Voltline Assemblies, Inc. Business Card

Voltline has three operating entities and I'm looking for a standard business card template that can be used for Voltline and the three operating entities that the logo just get swapped out, but has a very similar look and feel. Ultimately if someone had a business card from each, they assume the organizations are related because they all have the same look and feel.
Below are our websites and I will attached the logos for each entity:
https://www.voltlineassemblies.example/
https://www.brantoceramic.example/
https://www.omra-kfsd.example/
https://www.summitbreaker.example/

Target Market(s)

US Voltline

Industry/Entity Type

US Voltline

Contact Information for Business Card

Normal stuff

```html
<!DOCTYPE html>
<html lang="en">
<head>
<meta charset="utf-8">
<title>Voltline Assemblies, Inc. Business Cards</title>
<link rel="stylesheet" href="https://fonts.googleapis.com/css2?family=Open+Sans:wght@400;600;700&family=Rubik:wght@500;700;900&family=Roboto:wght@400;500;700&display=swap">
<style>
  :root{
    --page:#d7d7d7;
    --white:#ffffff;
    --v-navy:#1f2a5c;
    --v-red:#c0283a;
    --v-top-a:#7c2350;
    --v-top-b:#46295c;
    --v-bot-a:#b3233c;
    --v-bot-b:#6c2352;
    --o-navy:#17176e;
    --o-yellow:#f3e52a;
    --o-top-a:#7c7a4c;
    --o-top-b:#c6be3a;
    --o-bot-a:#2a2a6c;
    --o-bot-b:#8c8a3a;
    --s-slate:#5e7389;
    --s-dark:#444446;
    --s-text:#3a3f47;
    --b-blue:#4f86c6;
    --b-gray:#5c6168;
    --b-text:#2b3a55;
    --b-icon:#4a4a4c;
  }
  *{box-sizing:border-box;margin:0;padding:0}
  html,body{width:1200px;height:809px;overflow:hidden}
  body{background:var(--page);position:relative;font-family:"Open Sans",sans-serif}

  .card{position:absolute;width:403px;height:230px;background:var(--white);overflow:hidden}
  .card--voltline{left:122px;top:111px}
  .card--omra{left:675px;top:111px}
  .card--summit{left:122px;top:468px}
  .card--branto{left:675px;top:468px}

  .card__bg{position:absolute;inset:0;width:403px;height:230px}

  .logo{position:absolute;left:27px;top:24px;display:flex;align-items:center;gap:8px}
  .logo__mark{flex:none}
  .logo__name{font-weight:700;white-space:nowrap;line-height:1}
  .logo__parent{position:absolute;font-size:6.3px;white-space:nowrap;line-height:1}

  .holder{position:absolute;right:52px;top:108px;text-align:right}
  .holder__name{font-size:16.5px;font-weight:700;line-height:1}
  .holder__title{font-size:6.8px;font-weight:600;letter-spacing:1.6px;margin-top:5px;margin-right:-1.6px}

  .contact{position:absolute;right:25px;top:154px;list-style:none}
  .contact__row{display:flex;align-items:center;justify-content:flex-end;height:19px;gap:10px}
  .contact__text{font-size:9.4px;font-weight:600;white-space:nowrap}
  .contact__text--phone{letter-spacing:1.3px}
  .contact__icon{width:17px;height:17px;flex:none}

  .address{position:absolute;left:25px;color:var(--white)}
  .address__icon{width:17px;height:17px;display:block;margin-bottom:7px}
  .address__text{font-size:7.6px;font-weight:600;line-height:1.3;white-space:nowrap}

  /* Voltline */
  .card--voltline .logo{top:17px}
  .card--voltline .logo__name{font-size:15px;line-height:1.1;color:var(--v-navy)}
  .card--voltline .holder__name{color:var(--v-navy)}
  .card--voltline .holder__title,
  .card--voltline .contact__text{color:var(--v-red)}
  .card--voltline .contact__text--phone{color:var(--v-navy)}
  .card--voltline .contact__icon{color:var(--v-navy)}
  .card--voltline .address{top:150px}

  /* Omra */
  .card--omra{font-family:"Roboto",sans-serif}
  .card--omra .logo{top:28px;left:22px}
  .card--omra .logo__name{font-family:"Rubik",sans-serif;font-size:12.5px;font-weight:700;color:var(--o-navy)}
  .card--omra .logo__parent{left:105px;top:63px;color:var(--o-navy);font-weight:500}
  .card--omra .holder__name{font-family:"Rubik",sans-serif;font-weight:900;letter-spacing:1.2px;color:var(--o-navy)}
  .card--omra .holder__title{color:var(--o-navy);font-family:"Roboto",sans-serif;font-weight:500}
  .card--omra .contact__text{color:var(--o-navy);font-family:"Roboto",sans-serif;font-weight:500}
  .card--omra .contact__text--phone{font-family:"Rubik",sans-serif;font-weight:900;letter-spacing:2.2px}
  .card--omra .contact__icon{color:var(--o-navy)}
  .card--omra .address{top:126px;color:var(--o-yellow)}
  .card--omra .address__text{font-family:"Roboto",sans-serif;font-weight:500;font-size:7.3px}
  .card--omra .address__text + .address__text{margin-top:9px}

  /* Summit */
  .card--summit .logo{left:34px;top:30px}
  .card--summit .logo__name{font-size:14px;color:var(--s-slate)}
  .card--summit .logo__parent{left:105px;top:62px;color:var(--s-slate);font-weight:700}
  .card--summit .logo__rule{position:absolute;left:14px;height:1px;width:230px;background:var(--s-slate)}
  .card--summit .holder__name{color:var(--s-slate)}
  .card--summit .holder__title{color:var(--s-text);font-weight:400}
  .card--summit .contact__text{color:var(--s-text);font-weight:400}
  .card--summit .contact__text--phone{color:var(--s-slate);font-weight:600}
  .card--summit .contact__icon{color:var(--s-slate)}
  .card--summit .address{top:155px}
  .card--summit .address__text{font-size:8.2px;line-height:1.45}

  /* Branto */
  .card--branto{font-family:"Roboto",sans-serif}
  .card--branto .logo{left:25px;top:17px;gap:18px}
  .card--branto .logo__name{font-size:13.5px;color:var(--o-navy);font-family:"Roboto",sans-serif;margin-top:-10px}
  .card--branto .logo__parent{left:95px;top:52px;color:var(--o-navy);font-weight:500}
  .card--branto .holder__name{color:var(--b-gray);font-family:"Roboto",sans-serif;font-weight:500;font-size:17px}
  .card--branto .holder__title{color:var(--b-text);font-weight:500}
  .card--branto .contact__text{color:var(--b-text);font-weight:500;font-family:"Roboto",sans-serif}
  .card--branto .contact__text--phone{color:var(--b-gray)}
  .card--branto .contact__icon{color:var(--b-icon)}
  .card--branto .address{top:143px}
  .card--branto .address__text{font-family:"Roboto",sans-serif;font-weight:500;font-size:7.3px}
</style>
</head>
<body>

<svg width="0" height="0" style="position:absolute" aria-hidden="true">
  <defs>
    <symbol id="icon-mail" viewBox="0 0 17 17">
      <rect width="17" height="17" rx="2.5" fill="currentColor"/>
      <rect x="3" y="5" width="11" height="7.5" rx="0.8" fill="none" stroke="#fff" stroke-width="1"/>
      <text x="8.5" y="11.4" font-size="7" text-anchor="middle" fill="#fff" font-family="Arial,sans-serif">@</text>
    </symbol>
    <symbol id="icon-phone" viewBox="0 0 17 17">
      <rect width="17" height="17" rx="2.5" fill="currentColor"/>
      <rect x="5" y="2.5" width="7" height="12" rx="1.2" fill="none" stroke="#fff" stroke-width="1.2"/>
      <rect x="6.4" y="4.5" width="4.2" height="7" fill="#fff"/>
    </symbol>
    <symbol id="icon-web" viewBox="0 0 17 17">
      <rect width="17" height="17" rx="2.5" fill="currentColor"/>
      <circle cx="8.5" cy="8.5" r="5.3" fill="none" stroke="#fff" stroke-width="1.1"/>
      <path d="M3.2 8.5H13.8M8.5 3.2C6 6 6 11 8.5 13.8M8.5 3.2C11 6 11 11 8.5 13.8" fill="none" stroke="#fff" stroke-width="0.8"/>
    </symbol>
    <symbol id="icon-home" viewBox="0 0 17 17">
      <rect width="17" height="17" rx="2.5" fill="currentColor"/>
      <path d="M4 8.5L8.5 4.5L13 8.5V13H10.2V10H6.8V13H4Z" fill="var(--home-glyph,#555)"/>
    </symbol>
  </defs>
</svg>

<!-- Voltline card -->
<article class="card card--voltline">
  <svg class="card__bg" viewBox="0 0 403 230" aria-hidden="true">
    <defs>
      <linearGradient id="v-top" x1="0" y1="0" x2="1" y2="0">
        <stop offset="0" stop-color="var(--v-top-a)"/><stop offset="1" stop-color="var(--v-top-b)"/>
      </linearGradient>
      <linearGradient id="v-bot" x1="0" y1="0" x2="1" y2="1">
        <stop offset="0" stop-color="var(--v-bot-a)"/><stop offset="1" stop-color="var(--v-bot-b)"/>
      </linearGradient>
    </defs>
    <path d="M251 0H403V86H251C276 65 276 21 251 0Z" fill="url(#v-top)"/>
    <path d="M0 101H155C118 130 118 201 155 230H0Z" fill="url(#v-bot)"/>
  </svg>
  <div class="logo">
    <svg class="logo__mark" width="52" height="52" viewBox="0 0 52 52" aria-hidden="true"><circle cx="26" cy="26" r="26" fill="var(--v-navy)"/></svg>
    <span class="logo__name">Voltline<br>Assemblies, Inc.</span>
  </div>
  <div class="holder">
    <p class="holder__name">Daniel Ashford</p>
    <p class="holder__title">CEO / BOARD MEMBER</p>
  </div>
  <ul class="contact">
    <li class="contact__row"><span class="contact__text">daniel@voltlineassemblies.example</span><svg class="contact__icon"><use href="#icon-mail"/></svg></li>
    <li class="contact__row"><span class="contact__text contact__text--phone">1 (555) 014-2287</span><svg class="contact__icon"><use href="#icon-phone"/></svg></li>
    <li class="contact__row"><span class="contact__text">www.voltlineassemblies.example</span><svg class="contact__icon"><use href="#icon-web"/></svg></li>
  </ul>
  <div class="address" style="--home-glyph:var(--v-bot-a)">
    <svg class="address__icon" style="color:#fff"><use href="#icon-home"/></svg>
    <p class="address__text">Corporate Office:<br>4820 Ridgeway Drive<br>Suite 210<br>Fairmont, AL 35900</p>
  </div>
</article>

<!-- Omra card -->
<article class="card card--omra">
  <svg class="card__bg" viewBox="0 0 403 230" aria-hidden="true">
    <defs>
      <linearGradient id="o-top" x1="0" y1="0" x2="1" y2="0">
        <stop offset="0" stop-color="var(--o-top-a)"/><stop offset="1" stop-color="var(--o-top-b)"/>
      </linearGradient>
      <linearGradient id="o-bot" x1="0" y1="0" x2="1" y2="1">
        <stop offset="0" stop-color="var(--o-bot-a)"/><stop offset="1" stop-color="var(--o-bot-b)"/>
      </linearGradient>
    </defs>
    <path d="M263 0H403V86H263C288 65 288 21 263 0Z" fill="url(#o-top)"/>
    <path d="M0 96H170C126 128 126 198 164 230H0Z" fill="url(#o-bot)"/>
  </svg>
  <div class="logo">
    <svg class="logo__mark" width="22" height="22" viewBox="0 0 22 22" aria-hidden="true"><rect width="22" height="22" rx="4" fill="var(--o-navy)"/></svg>
    <span class="logo__name">Omra Transformer Devices Corp.</span>
  </div>
  <p class="logo__parent">A Voltline Assemblies, Inc. Company</p>
  <div class="holder">
    <p class="holder__name">Daniel Ashford</p>
    <p class="holder__title">CEO / BOARD MEMBER</p>
  </div>
  <ul class="contact">
    <li class="contact__row"><span class="contact__text">daniel@omra-kfsd.example</span><svg class="contact__icon"><use href="#icon-mail"/></svg></li>
    <li class="contact__row"><span class="contact__text contact__text--phone">1 (555) 014-2287</span><svg class="contact__icon"><use href="#icon-phone"/></svg></li>
    <li class="contact__row"><span class="contact__text">www.omra-kfsd.example</span><svg class="contact__icon"><use href="#icon-web"/></svg></li>
  </ul>
  <div class="address" style="--home-glyph:var(--o-bot-a)">
    <svg class="address__icon" style="color:var(--o-yellow)"><use href="#icon-home"/></svg>
    <p class="address__text">Sales,<br>Technical Support<br>&amp; Customer Service:</p>
    <p class="address__text">Omra, Inc.<br>PO Box 417<br>Ashby, NC 28900</p>
  </div>
</article>

<!-- Summit card -->
<article class="card card--summit">
  <svg class="card__bg" viewBox="0 0 403 230" aria-hidden="true">
    <path d="M266 0H403V86H266C291 65 291 21 266 0Z" fill="var(--s-slate)"/>
    <path d="M268 72H378L403 86H257C262 82 265 77 268 72Z" fill="var(--s-dark)"/>
    <path d="M0 101H155C118 130 118 201 155 230H0Z" fill="var(--s-slate)"/>
    <path d="M0 101H155C146 108 139 118 134 130H27L0 116Z" fill="var(--s-dark)"/>
  </svg>
  <span class="logo__rule" style="top:29px"></span>
  <span class="logo__rule" style="top:60px"></span>
  <div class="logo">
    <svg class="logo__mark" width="28" height="28" viewBox="0 0 28 28" aria-hidden="true"><rect width="28" height="28" fill="var(--s-slate)"/></svg>
    <span class="logo__name">SUMMIT BREAKER</span>
  </div>
  <p class="logo__parent">A Voltline Assemblies Inc. Company</p>
  <div class="holder">
    <p class="holder__name">Daniel Ashford</p>
    <p class="holder__title">CEO / BOARD MEMBER</p>
  </div>
  <ul class="contact">
    <li class="contact__row"><span class="contact__text">daniel@summitbreaker.example</span><svg class="contact__icon"><use href="#icon-mail"/></svg></li>
    <li class="contact__row"><span class="contact__text contact__text--phone">1 (555) 014-2287</span><svg class="contact__icon"><use href="#icon-phone"/></svg></li>
    <li class="contact__row"><span class="contact__text">www.summitbreaker.example</span><svg class="contact__icon"><use href="#icon-web"/></svg></li>
  </ul>
  <div class="address" style="--home-glyph:var(--s-slate)">
    <svg class="address__icon" style="color:#fff"><use href="#icon-home"/></svg>
    <p class="address__text">Postal address:<br>2716 Cedar Lane SE<br>Fairmont, AL 35900</p>
  </div>
</article>

<!-- Branto card -->
<article class="card card--branto">
  <svg class="card__bg" viewBox="0 0 403 230" aria-hidden="true">
    <defs>
      <linearGradient id="b-top" x1="0" y1="0" x2="0" y2="1">
        <stop offset="0" stop-color="#9a9c9f"/><stop offset="0.35" stop-color="#f2f2f2"/>
        <stop offset="0.7" stop-color="#c9d6e6"/><stop offset="1" stop-color="#7fa6d6"/>
      </linearGradient>
      <linearGradient id="b-thread" x1="0" y1="0" x2="0" y2="1">
        <stop offset="0" stop-color="#d8d8d8"/><stop offset="0.5" stop-color="#8c8c8c"/><stop offset="1" stop-color="#cfcfcf"/>
      </linearGradient>
    </defs>
    <path d="M260 0H403V77H256C281 56 281 21 260 0Z" fill="url(#b-top)" stroke="#444" stroke-width="1"/>
    <path d="M0 91H164C123 120 120 196 156 230H0Z" fill="var(--b-blue)"/>
    <path d="M0 91H164C153 99 144 110 137 127H0Z" fill="#dfe3e8"/>
    <rect role="img" aria-label="Threaded ceramic insulator bolt" x="18" y="95" width="118" height="30" fill="url(#b-thread)"/>
  </svg>
  <div class="logo">
    <svg class="logo__mark" width="52" height="52" viewBox="0 0 52 52" aria-hidden="true"><rect width="52" height="52" fill="var(--b-gray)"/></svg>
    <span class="logo__name">BRANTO CERAMIC, LLC.</span>
  </div>
  <p class="logo__parent">A Voltline Assemblies, Inc. Company</p>
  <div class="holder">
    <p class="holder__name">Daniel Ashford</p>
    <p class="holder__title">CEO / BOARD MEMBER</p>
  </div>
  <ul class="contact">
    <li class="contact__row"><span class="contact__text">daniel@brantoceramic.example</span><svg class="contact__icon"><use href="#icon-mail"/></svg></li>
    <li class="contact__row"><span class="contact__text contact__text--phone">1 (555) 014-2287</span><svg class="contact__icon"><use href="#icon-phone"/></svg></li>
    <li class="contact__row"><span class="contact__text">www.brantoceramic.example</span><svg class="contact__icon"><use href="#icon-web"/></svg></li>
  </ul>
  <div class="address" style="--home-glyph:var(--b-blue)">
    <svg class="address__icon" style="color:#fff"><use href="#icon-home"/></svg>
    <p class="address__text">Postal address:<br>518 W. County RT 9,<br>Ste 2, PO Box 73;<br>Hollis OH,<br>USA, 44900</p>
  </div>
</article>

</body>
</html>
```